Progressive European Honey Business needs minimalistic packaging design

Hello - thank you for your interest in our brief. We are Fizzy Vixens, a London based Honey business, importing only the best honey Europe has to offer. Our values are deeply rooted with in progressive liberal values and we are looking for minimalist packaging, which reflects that.

We are looking for a design, which dimensions fit with our packaging option (Velmor Glass Jar | HEIGHT 90mm | DIAMETER 63mm). We will require a various output files (High Resolution JPEG (CMYK Colors 300 dpi) Source File Ai, PSD, PDF, Printing files (die cut, die folding) and a 3D Mockup of the packaging for use within digital commerce platforms.

We must be able to adjust the free text on the label front and it should include the following:
Brand Name
Honey type
Limited edition No. X / 100 ( X being the number of purchase i.e. 25 / 100)
EU Honey, Single Orgin (Germany)
(c) The net weight (250g)

The back must include room for additional information (again adjustable by us) and the following:
“Unsuitable for children under 12 months”
(b) The appropriate durability declaration

In total, we are looking for
a) A front label
b) A back label
c) A seal (round) including the attached bee and logo included in the Zip file.
Do note that a) & b) can also be combined into one design as long as the symmetry on the jar stays intact.

The final design should communicate modern aesthetics, high quality, that are slightly provocative and pop off the shelves.

Hi folks, sorry for the delay in completing this project, but my business partner had a leak in his house. We planned to finalise our review today, but this will have to wait until it's no longer raining in his livingroom. Our sincere apologies!

• See branding guidelines

• Must follow the branding guideline and fonts provided as attachment

```html
<!DOCTYPE html>
<html lang="en">
<head>
<meta charset="utf-8">
<title>Fizzy Vixens – Front Label</title>
<link rel="stylesheet" href="https://fonts.googleapis.com/css2?family=Rammetto+One&family=Rozha+One&family=Montserrat:wght@700&family=Antonio:wght@300&display=swap">
<style>
  :root {
    --paper: #f4f4f4;
    --paper-shade: #e2e2e2;
    --brand-orange: #d9481c;
    --plum: #7a2a78;
    --plum-deep: #4f1a52;
    --ink: #141414;
    --honey: #f2c438;
    --bloom: #f2b08a;
  }
  * { margin: 0; padding: 0; box-sizing: border-box; }
  html, body { width: 1200px; height: 881px; overflow: hidden; background: #ffffff; }
  .label {
    position: relative;
    width: 1200px;
    height: 881px;
    background: radial-gradient(ellipse at 40% 40%, var(--paper) 0%, var(--paper-shade) 100%);
    overflow: hidden;
  }
  .mascot-art {
    position: absolute;
    left: 30px; top: 60px;
    width: 520px; height: 780px;
    border-radius: 40% 40% 30% 30%;
    background: radial-gradient(circle at 45% 40%, var(--honey) 0%, #2a2a2a 55%, var(--plum) 100%);
  }
  .bloom-art {
    position: absolute;
    right: 0; top: 0;
    width: 420px; height: 260px;
    border-bottom-left-radius: 60%;
    background: radial-gradient(circle at 50% 45%, var(--bloom) 0%, rgba(242,176,138,0.35) 60%, rgba(242,176,138,0) 100%);
  }
  .label-copy {
    position: absolute;
    right: 50px; top: 285px;
    text-align: right;
  }
  .brand-name {
    font-family: "Rammetto One", sans-serif;
    font-size: 52px;
    color: var(--brand-orange);
    letter-spacing: 1px;
    line-height: 1;
  }
  .honey-type {
    margin-top: 38px;
    font-family: "Rozha One", serif;
    font-size: 110px;
    line-height: 0.86;
    color: var(--plum);
  }
  .edition {
    margin-top: 36px;
    font-family: "Montserrat", sans-serif;
    font-weight: 700;
    font-size: 27px;
    color: var(--ink);
  }
  .origin {
    margin-top: 22px;
    font-family: "Antonio", sans-serif;
    font-weight: 300;
    font-size: 28px;
    line-height: 1.3;
    color: var(--ink);
  }
  .net-weight {
    margin-top: 36px;
    font-family: "Rozha One", serif;
    font-size: 28px;
    color: var(--plum);
  }
</style>
</head>
<body>
  <div class="label">
    <div class="bloom-art" role="img" aria-label="Watercolour hibiscus flowers in peach and orange"></div>
    <div class="mascot-art" role="img" aria-label="Cartoon queen bee mascot with a golden crown, blue wings and a black cape, in front of yellow and purple circles"></div>
    <div class="label-copy">
      <p class="brand-name">FIZZY VIXENS</p>
      <h1 class="honey-type">HONEY<br>TYPE</h1>
      <p class="edition">LIMITED EDITION NO. X / 100</p>
      <p class="origin">EU HONEY<br>SINGLE ORGIN<br>(GERMANY)</p>
      <p class="net-weight">The net weight (250g)</p>
    </div>
  </div>
</body>
</html>
```